Quillstone Business Card

We need a business card design. We have a logo from a previous Sketchfold project and I am attaching the logo files in jpeg and photoshop.

```html
<!DOCTYPE html>
<html lang="en">
<head>
<meta charset="utf-8">
<title>Quillstone Business Card</title>
<link href="https://fonts.googleapis.com/css2?family=Lato:wght@400;700&display=swap" rel="stylesheet">
<style>
  :root {
    --brand-green: #4db24a;
    --panel-dark: #323034;
    --panel-light: #f0f0f0;
    --paper: #ffffff;
    --ink: #555555;
    --ink-light: #ffffff;
  }
  * { margin: 0; padding: 0; box-sizing: border-box; }
  html, body {
    width: 1200px;
    height: 720px;
    overflow: hidden;
    background: var(--paper);
  }
  .card {
    position: relative;
    width: 1200px;
    height: 720px;
    background: var(--paper);
    font-family: "Lato", Arial, sans-serif;
  }
  .card-shapes {
    position: absolute;
    inset: 0;
  }
  .brand {
    position: absolute;
    left: 100px;
    top: 250px;
    width: 420px;
    height: 72px;
    display: flex;
    align-items: center;
    gap: 18px;
  }
  .brand-mark {
    width: 44px;
    height: 44px;
    background: var(--brand-green);
    flex: none;
  }
  .brand-name {
    color: var(--ink-light);
    font-weight: 700;
    font-size: 60px;
    letter-spacing: -0.5px;
    line-height: 1;
  }
  .person {
    position: absolute;
    right: 83px;
    top: 96px;
    text-align: right;
    color: var(--ink-light);
  }
  .person-name {
    font-weight: 700;
    font-size: 36px;
    line-height: 44px;
  }
  .person-role {
    font-weight: 400;
    font-size: 21px;
    line-height: 26px;
  }
  .address {
    position: absolute;
    left: 880px;
    width: 200px;
    top: 338px;
    text-align: center;
    color: var(--ink);
    font-size: 21px;
  }
  .contact-group {
    position: absolute;
    right: 158px;
    text-align: right;
    color: var(--ink);
    font-size: 21px;
    line-height: 31px;
  }
  .contact-phone { top: 418px; }
  .contact-web { top: 510px; }
</style>
</head>
<body>
  <div class="card">
    <svg class="card-shapes" width="1200" height="720" viewBox="0 0 1200 720" aria-hidden="true">
      <polygon class="panel-dark" points="0,0 387,0 539,288 317,720 0,720" fill="var(--panel-dark)"/>
      <polygon class="panel-green" points="405,0 1200,0 1200,286 557,286" fill="var(--brand-green)"/>
      <polygon class="panel-light" points="557,302 1200,302 1200,720 334,720" fill="var(--panel-light)"/>

      <line class="contact-rule" x1="600" y1="448" x2="1060" y2="448" stroke="var(--brand-green)" stroke-width="2"/>
      <line class="contact-rule" x1="600" y1="543" x2="1060" y2="543" stroke="var(--brand-green)" stroke-width="2"/>

      <g class="icon-phone" transform="translate(1086,449)">
        <polygon points="-34,0 -17,-32 17,-32 34,0 17,32 -17,32" fill="var(--brand-green)"/>
        <path d="M-16,-6 Q-16,-14 0,-14 Q16,-14 16,-6 L10,-6 L10,-9 L-10,-9 L-10,-6 Z" fill="var(--ink-light)"/>
        <path d="M-9,-4 L9,-4 L13,13 L-13,13 Z" fill="var(--ink-light)"/>
        <g fill="var(--brand-green)">
          <rect x="-5" y="0" width="2.5" height="2.5"/><rect x="-1.2" y="0" width="2.5" height="2.5"/><rect x="2.6" y="0" width="2.5" height="2.5"/>
          <rect x="-5" y="4" width="2.5" height="2.5"/><rect x="-1.2" y="4" width="2.5" height="2.5"/><rect x="2.6" y="4" width="2.5" height="2.5"/>
          <rect x="-5" y="8" width="2.5" height="2.5"/><rect x="-1.2" y="8" width="2.5" height="2.5"/><rect x="2.6" y="8" width="2.5" height="2.5"/>
        </g>
      </g>

      <g class="icon-monitor" transform="translate(1086,544)">
        <polygon points="-34,0 -17,-32 17,-32 34,0 17,32 -17,32" fill="var(--brand-green)"/>
        <rect x="-16" y="-14" width="32" height="23" fill="var(--ink-light)"/>
        <rect x="-12" y="-10" width="24" height="15" fill="var(--brand-green)"/>
        <rect x="-2" y="9" width="4" height="5" fill="var(--ink-light)"/>
        <rect x="-8" y="13" width="16" height="3" fill="var(--ink-light)"/>
      </g>
    </svg>

    <div class="brand">
      <span class="brand-mark"></span>
      <span class="brand-name">Quillstone</span>
    </div>

    <div class="person">
      <p class="person-name">NAME SURNAME</p>
      <p class="person-role">Your Position</p>
    </div>

    <p class="address">Address</p>

    <div class="contact-group contact-phone">
      <p>+ 000 - 1234 - 5678</p>
      <p>+ 000 - 9876 - 5432</p>
    </div>

    <div class="contact-group contact-web">
      <p>your@email.com</p>
      <p>yourwebsite.com</p>
    </div>
  </div>
</body>
</html>
```